We need a design for a contracting company website based in KSA, something modern with the same color theme as the attached logo. including a page for people who want to submit their CV and try to apply for a job.Also to include the "about us, contact us, gallery, Divisions, Supplies, etc...". If possible to have an interactive or moving background. Please disregard the "Bright Pathways" Section in the attached profile.

Industry/Entity Type

Construction Company

Number of Pages Required

5+ page

Colors

Designer to choose colors to be used in the design.

Requirements
Must have
• Pages:
• about us, contact us, gallery, Divisions, Apply for a job, Supplies
Nice to have
• - Moving or interactive background

```html
<!DOCTYPE html>
<html lang="en">
<head>
<meta charset="utf-8">
<title>Cobaltine Building Company</title>
<link rel="stylesheet" href="https://fonts.googleapis.com/css2?family=Poppins:wght@400;500;600;700&family=Open+Sans:wght@400;600&display=swap">
<style>
:root{
  --yellow:#f7b500;
  --yellow-deep:#eca800;
  --ink:#1f1f1f;
  --text:#6b6b6b;
  --muted:#9a9a9a;
  --line:#e4e4e4;
  --paper:#ffffff;
  --soft:#f3f3f3;
  --footer:#1b1b1b;
  --footer-2:#141414;
}
*{box-sizing:border-box;margin:0;padding:0}
html,body{width:1200px;height:3748px;overflow:hidden;background:var(--paper)}
body{font-family:"Open Sans",Arial,sans-serif;color:var(--text);font-size:13px;line-height:1.7;position:relative}
h1,h2,h3,h4,.brand,.btn,.nav a{font-family:"Poppins",Arial,sans-serif}
.abs{position:absolute}
.ph{position:absolute}
.btn{display:inline-block;background:var(--yellow);color:var(--ink);font-weight:600;font-size:12px;border-radius:20px;padding:9px 24px;letter-spacing:.3px}

/* header / hero */
.hero{position:absolute;left:0;top:0;width:1200px;height:620px;overflow:hidden}
.hero-photo{left:0;top:0;width:1200px;height:620px;background:linear-gradient(160deg,#5b5d60 0%,#9c9ea0 35%,#d9dadb 65%,#efefef 100%)}
.hero-arc{position:absolute;left:0;bottom:0}
.site-header{position:absolute;left:0;top:0;width:1200px;height:80px}
.logo{position:absolute;left:130px;top:14px;display:flex;align-items:center;gap:10px}
.logo-mark{width:34px;height:44px;background:var(--yellow)}
.brand{color:#fff;font-size:22px;font-weight:600;letter-spacing:1px}
.nav{position:absolute;left:460px;top:22px;display:flex;gap:26px;align-items:center}
.nav a{font-size:12px;color:#2a2a2a;text-decoration:none;font-weight:500}
.nav a.active{color:var(--yellow-deep);border-bottom:2px solid var(--yellow);padding-bottom:4px}
.nav .btn{padding:7px 18px;font-size:11px;border-radius:3px}

/* about */
.about-photo{left:232px;top:608px;width:248px;height:344px;background:linear-gradient(180deg,#d7dadd,#a1a6ab 60%,#d08a2c)}
.about-text{left:580px;top:620px;width:392px}
h2{color:var(--ink);font-size:26px;font-weight:600;line-height:1.25}
.about-text p{margin-top:14px;font-size:12px}
.about-text .btn{margin-top:22px}

/* why */
.why{left:0;top:952px;width:1200px;height:336px;background:var(--soft)}
.why-text{left:232px;top:42px;width:430px}
.why-text p{margin-top:12px;font-size:12px}
.ticks{list-style:none;margin-top:14px}
.ticks li{display:flex;align-items:center;gap:10px;font-size:12px;color:#444;margin-bottom:8px}
.why-video{left:752px;top:40px;width:220px;height:228px;background:linear-gradient(180deg,#7aa9cf,#a9c3d8 55%,#8a8378)}
.play{position:absolute;left:86px;top:90px;width:48px;height:48px;border-radius:50%;background:var(--yellow);display:flex;align-items:center;justify-content:center}

/* services */
.services{left:0;top:1288px;width:1200px;height:380px}
.service{position:absolute;top:72px;width:200px;text-align:center}
.circle{width:100px;height:100px;border-radius:50%;border:2px solid var(--line);margin:0 auto;display:flex;align-items:center;justify-content:center;background:#fff}
.circle.on{background:var(--yellow);border-color:var(--yellow)}
.service h4{margin-top:14px;font-size:13px;font-weight:600;color:var(--ink)}
.arrows{position:absolute;left:568px;top:290px;display:flex;gap:8px}
.arrows span{width:22px;height:22px;border:1px solid #999;display:flex;align-items:center;justify-content:center}

/* projects */
.projects-title{left:232px;top:1706px}
.filter{left:232px;top:1768px;list-style:none}
.filter li{font-size:12px;color:#555;margin-bottom:10px;display:flex;gap:6px;align-items:center}
.filter li:first-child{color:var(--yellow-deep);font-weight:600}
.filter li::before{content:"";width:5px;height:5px;background:currentColor;border-radius:50%}

/* experience band */
.band{left:0;top:2400px;width:1200px;height:220px;background:var(--yellow);text-align:center}
.band h2{margin-top:44px;font-size:26px}
.band p{width:620px;margin:10px auto 0;color:#3a3000;font-size:12px}
.band-row{display:flex;justify-content:center;align-items:center;gap:26px;margin-top:22px}
.band-phone{font-family:"Poppins",sans-serif;font-weight:700;font-size:24px;color:var(--ink)}
.btn.dark{background:var(--ink);color:#fff}

/* testimonials */
.testi-title{left:0;top:2690px;width:1200px;text-align:center}
.testi{position:absolute;top:2770px;width:360px}
.avatar{position:absolute;left:0;top:0;width:56px;height:56px;border-radius:50%;background:linear-gradient(135deg,#d9c6b3,#a8927e)}
.testi p{margin-left:80px;font-size:12px}
.testi h4{margin:10px 0 0 80px;font-size:12px;color:var(--ink);font-weight:600}
.testi small{display:block;margin-left:80px;color:var(--yellow-deep);font-size:11px}

/* contact */
.contact{left:0;top:2960px;width:1200px;height:312px;background:var(--soft)}
.contact-photo{left:208px;top:48px;width:192px;height:276px;background:linear-gradient(180deg,#c9ccd0,#8c9399 60%,#cf8d35)}
.contact-card{left:420px;top:48px;width:240px}
.contact-card h3{font-size:22px;font-weight:700;color:var(--ink);line-height:1.15}
.contact-card h3 span{display:block;font-size:13px;font-weight:600}
.contact-card h4{margin-top:14px;font-size:14px;color:var(--ink);font-weight:600}
.contact-card .row{display:flex;gap:8px;align-items:center;font-size:11px;margin-top:6px}
.form{left:680px;top:40px;width:292px}
.form h2{font-size:22px}
.field{height:30px;border:1px solid var(--line);background:#fff;margin-top:10px;font-size:11px;padding:6px 10px;color:var(--muted)}
.field.area{height:72px}
.form .btn{margin-top:12px;padding:7px 22px;font-size:11px}

/* footer */
.footer{left:0;top:3272px;width:1200px;height:476px;background:var(--footer);color:#aaa}
.f-info{position:absolute;top:28px;display:flex;gap:12px;align-items:flex-start;font-size:11px}
.f-icon{width:30px;height:30px;border-radius:50%;background:var(--yellow);display:flex;align-items:center;justify-content:center;flex:none}
.f-rule{left:232px;top:90px;width:740px;height:1px;background:#333}
.f-col{position:absolute;top:120px;font-size:11px}
.f-col h4{color:#fff;font-size:13px;font-weight:600;margin-bottom:10px}
.f-col ul{list-style:none}
.f-col li{margin-bottom:4px}
.f-col li::before{content:"› ";color:var(--yellow)}
.social{display:flex;gap:8px;margin-top:12px}
.social span{width:20px;height:20px;border-radius:50%;background:#333}
.newsletter{height:28px;background:#2a2a2a;margin-top:8px;padding:5px 10px;color:#777}
.bottom-bar{left:0;top:404px;width:1200px;height:72px;background:var(--footer-2);font-size:10px;color:#777;padding:28px 232px}
</style>
</head>
<body>

<section class="hero">
  <div class="ph hero-photo" role="img" aria-label="Engineer's hands working over building plans on a desk"></div>
  <svg class="hero-arc" width="1200" height="70" viewBox="0 0 1200 70"><path d="M0 70 L0 30 Q600 -20 1200 30 L1200 70 Z" fill="#fff"/></svg>
  <header class="site-header">
    <div class="logo"><span class="logo-mark"></span><span class="brand">COBALTINE</span></div>
    <nav class="nav">
      <a class="active">Home</a><a>About Us</a><a>Services</a><a>Divisions</a><a>Supplies</a><a>Gallery</a><a>Contact</a>
      <span class="btn">Apply for a Job</span>
    </nav>
  </header>
</section>

<section>
  <div class="ph about-photo" role="img" aria-label="Site engineer in hard hat and safety vest holding a pen"></div>
  <div class="abs about-text">
    <h2>About Us</h2>
    <p>We are a building and contracting firm delivering residential, commercial and industrial projects across the Kingdom with quality, safety and care at the heart of every site we run.</p>
    <p>Our teams of engineers, planners and skilled crews manage each project from concept to handover, keeping budgets clear and schedules on time.</p>
    <span class="btn">Read More</span>
  </div>
</section>

<section class="abs why">
  <div class="abs why-text">
    <h2>Why you choose us for your<br>next project !</h2>
    <p>We bring years of field experience, trusted suppliers and a committed team to every job, so your project moves forward with confidence from day one.</p>
    <ul class="ticks">
      <li><svg width="14" height="14"><circle cx="7" cy="7" r="7" fill="#f7b500"/><path d="M4 7l2 2 4-4" stroke="#fff" stroke-width="1.6" fill="none"/></svg>Expert Professional Engineers</li>
      <li><svg width="14" height="14"><circle cx="7" cy="7" r="7" fill="#f7b500"/><path d="M4 7l2 2 4-4" stroke="#fff" stroke-width="1.6" fill="none"/></svg>We are Award Winning Firm</li>
      <li><svg width="14" height="14"><circle cx="7" cy="7" r="7" fill="#f7b500"/><path d="M4 7l2 2 4-4" stroke="#fff" stroke-width="1.6" fill="none"/></svg>Fully Satisfaction Guarantee</li>
      <li><svg width="14" height="14"><circle cx="7" cy="7" r="7" fill="#f7b500"/><path d="M4 7l2 2 4-4" stroke="#fff" stroke-width="1.6" fill="none"/></svg>1K+ Successful Projects done</li>
    </ul>
  </div>
  <div class="ph why-video" role="img" aria-label="Tower cranes over a building under construction">
    <span class="play"><svg width="16" height="18"><path d="M2 1l13 8-13 8z" fill="#1f1f1f"/></svg></span>
  </div>
</section>

<section class="abs services">
  <div class="service" style="left:190px"><div class="circle"><svg width="44" height="44" fill="none" stroke="#1f1f1f" stroke-width="2"><path d="M6 40V18l16-12 16 12v22z"/><rect x="17" y="26" width="10" height="14"/></svg></div><h4>Building Renovation</h4></div>
  <div class="service" style="left:384px"><div class="circle on"><svg width="44" height="44" fill="none" stroke="#fff" stroke-width="2"><rect x="8" y="14" width="28" height="26"/><path d="M4 14h36M14 22h6M24 22h6M14 30h6M24 30h6"/></svg></div><h4>Building Construction</h4></div>
  <div class="service" style="left:592px"><div class="circle"><svg width="44" height="44" fill="none" stroke="#1f1f1f" stroke-width="2"><rect x="6" y="16" width="14" height="24"/><rect x="22" y="6" width="16" height="34"/><path d="M26 12h8M26 20h8M26 28h8"/></svg></div><h4>Building Maintenance</h4></div>
  <div class="service" style="left:792px"><div class="circle"><svg width="44" height="44" fill="none" stroke="#1f1f1f" stroke-width="2"><path d="M6 40h32M10 40V20l12-10 12 10v20"/><path d="M16 40V28h12v12"/></svg></div><h4>Architecture Design</h4></div>
  <div class="arrows"><span><svg width="8" height="10"><path d="M7 1L2 5l5 4" stroke="#555" fill="none"/></svg></span><span><svg width="8" height="10"><path d="M1 1l5 4-5 4" stroke="#555" fill="none"/></svg></span></div>
</section>

<section>
  <h2 class="abs projects-title" style="font-size:22px">Our Projects</h2>
  <ul class="abs filter">
    <li>All Work</li><li>Residential</li><li>Commercial</li><li>Hospital</li><li>Office</li><li>Reconstruction</li><li>Residential</li>
  </ul>
  <div class="ph" style="left:360px;top:1768px;width:188px;height:184px;background:linear-gradient(180deg,#8fb6d8,#5d7893)" role="img" aria-label="Glass office tower"></div>
  <div class="ph" style="left:568px;top:1768px;width:188px;height:184px;background:linear-gradient(180deg,#c9d3dc,#4a4d52)" role="img" aria-label="Worker in hard hat on site"></div>
  <div class="ph" style="left:772px;top:1768px;width:200px;height:184px;background:linear-gradient(180deg,#e9b54a,#c79436)" role="img" aria-label="Finished interior with yellow wall"></div>
  <div class="ph" style="left:360px;top:1964px;width:188px;height:184px;background:linear-gradient(160deg,#d9d2c6,#a58f71)" role="img" aria-label="Hands reviewing construction drawings"></div>
  <div class="ph" style="left:568px;top:1964px;width:188px;height:184px;background:linear-gradient(180deg,#7aa8d6,#d3dadf)" role="img" aria-label="Mid-rise residential building"></div>
  <div class="ph" style="left:772px;top:1964px;width:200px;height:184px;background:linear-gradient(180deg,#8ab8e0,#b4563a)" role="img" aria-label="Brick apartment block"></div>
  <div class="ph" style="left:360px;top:2160px;width:188px;height:180px;background:linear-gradient(180deg,#c8c5c0,#6b6157)" role="img" aria-label="Builder with helmet at work"></div>
  <div class="ph" style="left:568px;top:2160px;width:188px;height:180px;background:linear-gradient(180deg,#e6e8ea,#6f8a5a)" role="img" aria-label="White apartment building with trees"></div>
  <div class="ph" style="left:772px;top:2160px;width:200px;height:180px;background:linear-gradient(180deg,#9ec6e6,#7d8f6d)" role="img" aria-label="Building frame under construction"></div>
</section>

<section class="abs band">
  <h2>We have 15 years experience in Construction</h2>
  <p>Fifteen years of steady growth, hundreds of delivered sites and a team that treats every client build as if it were our own home.</p>
  <div class="band-row"><span class="band-phone">1800.555.0142</span><span class="btn dark">Get appointment</span></div>
</section>

<section>
  <h2 class="abs testi-title">What our client says</h2>
  <div class="testi" style="left:232px">
    <div class="avatar" role="img" aria-label="Client portrait"></div>
    <p>The team handled our villa build with real care. Every stage was explained clearly, the site stayed tidy and the handover came right on schedule.</p>
    <h4>— Samuel Ortega</h4><small>Villa Owner</small>
  </div>
  <div class="testi" style="left:620px">
    <div class="avatar" role="img" aria-label="Client portrait"></div>
    <p>Professional engineers, honest pricing and quick answers to every question. We will trust them again for our next commercial project.</p>
    <h4>— Laila Mansour</h4><small>Property Manager</small>
  </div>
</section>

<section class="abs contact">
  <div class="ph contact-photo" role="img" aria-label="Site engineer in hard hat and vest"></div>
  <div class="abs contact-card">
    <h3>Cobaltine<span>Building Company</span></h3>
    <h4>Daniel Harlow</h4>
    <div class="row"><svg width="12" height="12"><circle cx="6" cy="6" r="6" fill="#f7b500"/></svg>1800.555.0142</div>
    <div class="row"><svg width="12" height="12"><circle cx="6" cy="6" r="6" fill="#f7b500"/></svg>hello@cobaltine-build.test</div>
    <h4>Office Time</h4>
    <div class="row">Sun – Thu : 8:00 am – 5:00 pm</div>
    <div class="row">Sat : 9:00 am – 1:00 pm</div>
  </div>
  <div class="abs form">
    <h2>Drop us mesage</h2>
    <div class="field">Your Name</div>
    <div class="field">Your Email</div>
    <div class="field">Phone Number</div>
    <div class="field area">Message</div>
    <span class="btn">Submit now</span>
  </div>
</section>

<footer class="abs footer">
  <div class="f-info" style="left:232px"><span class="f-icon"><svg width="12" height="14"><path d="M6 1a4 4 0 014 4c0 3-4 8-4 8S2 8 2 5a4 4 0 014-4z" fill="#1f1f1f"/></svg></span><span>Marble Street 24, Riyadh<br>P.O. Box 12345</span></div>
  <div class="f-info" style="left:500px"><span class="f-icon"><svg width="14" height="10"><rect x="1" y="1" width="12" height="8" fill="none" stroke="#1f1f1f" stroke-width="1.5"/><path d="M1 1l6 4 6-4" stroke="#1f1f1f" fill="none"/></svg></span><span>Email us :<br>hello@cobaltine-build.test</span></div>
  <div class="f-info" style="left:740px"><span class="f-icon"><svg width="12" height="12"><path d="M2 1h3l1 3-2 1a7 7 0 003 3l1-2 3 1v3c-6 0-9-3-9-9z" fill="#1f1f1f"/></svg></span><span>Call us :<br>1800.555.0142</span></div>
  <div class="abs f-rule"></div>
  <div class="f-col" style="left:232px;width:150px">
    <div style="display:flex;gap:8px;align-items:center;margin-bottom:12px"><span class="logo-mark" style="width:22px;height:28px"></span><span class="brand" style="font-size:16px">COBALTINE</span></div>
    <p>Building trusted homes and workplaces across the Kingdom with quality crews.</p>
    <div class="social"><span></span><span></span><span></span><span></span></div>
  </div>
  <div class="f-col" style="left:420px"><h4>Quick Links</h4><ul><li>About Us</li><li>Divisions</li><li>Supplies</li><li>Gallery</li><li>Apply for a Job</li></ul></div>
  <div class="f-col" style="left:600px"><h4>Our Services</h4><ul><li>Building Renovation</li><li>Building Construction</li><li>Building Maintenance</li><li>Architecture Design</li></ul></div>
  <div class="f-col" style="left:792px;width:180px"><h4>Newsletter</h4><p>Get project news and offers in your inbox.</p><div class="newsletter">Your Email</div><span class="btn" style="margin-top:8px;padding:5px 16px;font-size:10px">Subscribe now</span></div>
  <div class="abs bottom-bar">© Copyright by Cobaltine Building Company 2024. All rights reserved.</div>
</footer>

</body>
</html>
```